Quarvolindex Website

we need a web site similar to Pluvrex.com or Zantor7 com or halverpoint.com - Although our budget is small we would like to look like them. we are in the same industry
Updates
Reason: Can you do an exact copy of Pluvrex.com if so how long ? What do you require? What is the next step?Please let me know you can also email me at dorvilak@quenmoxa.com for faster answers.
Thank you
Target Market(s)
small and medium size business
Requirements
Must have
- product portfolio - just like Pluvrex.com
Nice to have
- ecomerce and mobile app

```html
<!DOCTYPE html>
<html lang="en">
<head>
<meta charset="utf-8">
<title>Quarvolindex</title>
<link rel="stylesheet" href="https://fonts.googleapis.com/css2?family=Michroma&family=Saira+Condensed:wght@600;800&family=Arimo:wght@400;700&family=Oswald:wght@300&display=swap">
<style>
:root{
  --ink:#3b3f45;
  --slate:#6b7583;
  --nav:#8c959e;
  --tile:#f0f0f0;
  --footer:#6e7985;
  --footer-text:#ffffff;
  --muted:#777b80;
  --link-blue:#1a5fa8;
}
*{margin:0;padding:0;box-sizing:border-box}
html,body{width:933px;height:1200px;overflow:hidden;background:#fff}
body{font-family:"Arimo",Arial,sans-serif;color:#222}
.page{position:relative;width:933px;height:1200px;overflow:hidden}

.site-header{position:absolute;left:0;top:0;width:933px;height:71px;background:#fff}
.brand{position:absolute;left:29px;top:20px;font-family:"Michroma",sans-serif;font-size:24px;letter-spacing:1px;color:var(--ink)}
.hotline{position:absolute;right:22px;top:15px;text-align:right}
.hotline-label{font-size:11px;color:#666;letter-spacing:.2px}
.hotline-number{display:flex;align-items:center;justify-content:flex-end;gap:7px;margin-top:2px;font-family:"Oswald",sans-serif;font-weight:300;font-size:25px;color:#333;line-height:1}

.main-nav{position:absolute;left:0;top:71px;width:933px;height:43px;background:var(--nav)}
.main-nav ul{list-style:none;display:flex;justify-content:space-between;align-items:center;height:100%;padding:0 38px}
.main-nav li{font-family:"Saira Condensed",sans-serif;font-weight:600;font-size:16px;color:#fff;text-transform:uppercase;white-space:nowrap}

.hero{position:absolute;left:0;top:114px;width:933px;height:361px;
  background:radial-gradient(circle at 58% 35%,#e6eef2 0%,#bfcdd6 25%,#93a4b0 55%,#707f8b 100%)}

.services{position:absolute;left:0;top:475px;width:933px;height:254px;display:grid;grid-template-columns:310px 310px 311px;grid-template-rows:126px 126px;gap:2px 1px;background:#e2e2e2}
.service{position:relative;background:var(--tile);overflow:hidden}
.service-icon{position:absolute;left:15px;top:21px;width:84px;height:84px;border-radius:50%;background:var(--slate);border:3px solid #fff;box-shadow:0 0 0 1px #d9d9d9;display:flex;align-items:center;justify-content:center}
.service-title{position:absolute;left:114px;top:39px;font-family:"Saira Condensed",sans-serif;font-weight:800;font-size:30px;line-height:32px;color:var(--ink);white-space:nowrap}
.service-link{position:absolute;left:116px;top:74px;font-size:11px;font-weight:700;color:var(--muted)}
.service-link.is-active{color:var(--link-blue)}

.why{position:absolute;left:21px;top:773px;width:895px}
.why h2{font-family:"Michroma",sans-serif;font-weight:400;font-size:21px;color:#5a6470;letter-spacing:.5px}
.why p{margin-top:14px;font-size:13.2px;line-height:16.3px;color:#111;padding-left:3px}
.why p + p{margin-top:16px}

.site-footer{position:absolute;left:0;top:979px;width:933px;height:221px;background:var(--footer);color:var(--footer-text)}
.footer-heading{font-family:"Saira Condensed",sans-serif;font-weight:800;font-size:19px;line-height:20px;text-transform:uppercase}
.footer-nav{position:absolute;left:29px;top:32px}
.footer-nav ul{list-style:none;margin-top:11px}
.footer-nav li{font-size:12px;line-height:15.3px}
.testimonial{position:absolute;left:308px;top:32px;width:320px}
.testimonial-icon{position:absolute;left:2px;top:33px}
.testimonial blockquote{position:absolute;left:57px;top:38px;width:255px;font-size:11.5px;line-height:14px}
.testimonial cite{position:absolute;left:2px;top:104px;font-style:normal;font-size:13.5px;white-space:nowrap}
.testimonial cite span{opacity:.6}
.contact{position:absolute;left:718px;top:32px;width:200px}
.social{display:flex;gap:8px;margin-top:13px}
.social span{width:26px;height:26px;border-radius:50%;background:#8f99a4;display:block}
.newsletter-note{margin-top:14px;font-size:10.5px;line-height:12.5px}
.newsletter-field{margin-top:10px;width:176px;height:25px;border-radius:13px;background:#ececec;color:#222;font-size:10.5px;line-height:25px;padding-left:14px}
.subscribe{margin-top:13px;font-size:10.5px;font-weight:700;display:flex;align-items:center;gap:6px;padding-left:2px}
</style>
</head>
<body>
<div class="page">
  <header class="site-header">
    <div class="brand">QUARVOLINDEX</div>
    <div class="hotline">
      <div class="hotline-label">FOR SERVICES &amp; INQUIRIES</div>
      <div class="hotline-number">
        <svg width="25" height="25" viewBox="0 0 26 26" aria-hidden="true"><circle cx="13" cy="13" r="11.5" fill="none" stroke="#333" stroke-width="2"/><path d="M9 7.5c.8-.6 1.6-.4 2 .3l1.1 2c.3.6.1 1.2-.4 1.6l-.8.6c.6 1.5 1.6 2.7 3 3.5l.7-.7c.5-.5 1.2-.5 1.7-.1l1.8 1.4c.6.5.6 1.3 0 1.9-1.4 1.4-3.3 1.2-5.1-.2-2.5-1.9-4.2-4.4-4.8-7-.3-1.4 0-2.6.8-3.3z" fill="#333"/></svg>
        012-5550147
      </div>
    </div>
  </header>

  <nav class="main-nav">
    <ul>
      <li>Home</li><li>About</li><li>Why Quarvolindex</li><li>Services</li><li>Solutions</li><li>Partners</li><li>Contact</li>
    </ul>
  </nav>

  <div class="hero" role="img" aria-label="Photo of a businessman in a suit touching a glowing digital interface while holding a smartphone, with floating binary digits"></div>

  <section class="services">
    <div class="service">
      <div class="service-icon"><svg width="50" height="50" viewBox="0 0 50 50" aria-hidden="true"><path d="M14 28a7 7 0 0 1 1-14 10 10 0 0 1 19-2 8 8 0 0 1 3 16z" fill="#fff"/><path d="M17 33q8 5 16 0M20 38q5 3 10 0" stroke="#fff" stroke-width="2.5" fill="none" stroke-linecap="round"/></svg></div>
      <div class="service-title">CLOUD &amp; DATA</div>
      <div class="service-link">Check Service</div>
    </div>
    <div class="service">
      <div class="service-icon"><svg width="46" height="46" viewBox="0 0 46 46" aria-hidden="true"><path d="M12 6c2-1.5 4-1 5 1l3 6c.6 1.5.2 2.8-1 3.6l-2 1.4c1 4 3.3 7.5 6.5 10l2-1.2c1.2-.7 2.6-.5 3.5.6l4 5c1 1.3.8 3-.6 4-4 3-9 1.5-13.5-3.5C13 28 10 21 10 14c0-3.5.6-6.3 2-8z" fill="#fff"/><path d="M29 20q4 3 3 8M32 17q6 4 4 12" stroke="#fff" stroke-width="2" fill="none"/></svg></div>
      <div class="service-title">VOICE &amp; PHONES</div>
      <div class="service-link">Check Service</div>
    </div>
    <div class="service">
      <div class="service-icon"><svg width="50" height="50" viewBox="0 0 50 50" aria-hidden="true"><path d="M13 24v-4a12 12 0 0 1 24 0v4" stroke="#fff" stroke-width="3" fill="none"/><rect x="10" y="21" width="6" height="10" rx="2" fill="#fff"/><rect x="34" y="21" width="6" height="10" rx="2" fill="#fff"/><path d="M37 31q0 6-9 7" stroke="#fff" stroke-width="2" fill="none"/><rect x="9" y="36" width="32" height="7" rx="3" fill="#fff"/></svg></div>
      <div class="service-title">NETWORK</div>
      <div class="service-link is-active">Check Service</div>
    </div>
    <div class="service">
      <div class="service-icon"><svg width="46" height="50" viewBox="0 0 46 50" aria-hidden="true"><rect x="11" y="5" width="24" height="40" rx="4" fill="none" stroke="#fff" stroke-width="3"/><rect x="15" y="11" width="16" height="26" fill="#fff"/><circle cx="23" cy="41" r="1.6" fill="#fff"/></svg></div>
      <div class="service-title">MOBILE</div>
      <div class="service-link">Check Service</div>
    </div>
    <div class="service">
      <div class="service-icon"><svg width="50" height="50" viewBox="0 0 50 50" aria-hidden="true"><path d="M25 6l17 8-17 8-17-8z" fill="#fff"/><path d="M7 17l16 8v19L7 36z" fill="#fff"/><path d="M43 17L27 25v19l16-8z" fill="#fff"/></svg></div>
      <div class="service-title">APPLICATIONS</div>
      <div class="service-link">Check Service</div>
    </div>
    <div class="service">
      <div class="service-icon"><svg width="54" height="50" viewBox="0 0 54 50" aria-hidden="true"><rect x="11" y="10" width="32" height="22" rx="2" fill="#fff"/><rect x="14" y="13" width="26" height="16" fill="none" stroke="#6b7583" stroke-width="1.5"/><path d="M17 20l5-5M17 24l8-8" stroke="#6b7583" stroke-width="2"/><path d="M6 34h42v2a2 2 0 0 1-2 2H8a2 2 0 0 1-2-2z" fill="#fff"/></svg></div>
      <div class="service-title">IT SERVICES</div>
      <div class="service-link">Check Service</div>
    </div>
  </section>

  <section class="why">
    <h2>WHY CHOOSE QUARVOLINDEX?</h2>
    <p>Lorem ipsum dolor sit amet, consectetur adipisicing elit, sed do eiusmod tempor incididunt ut labore et dolore magna aliqua. Ut enim ad minim veniam, quis nostrud exercitation ullamco laboris nisi ut aliquip ex ea commodo consequat. Duis aute irure dolor in reprehenderit in voluptate velit esse cillum dolore eu fugiat nulla pariatur. Excepteur sint occaecat cupidatat non proident, sunt in culpa qui officia deserunt mollit anim id est laborum.</p>
    <p>Sed ut perspiciatis, unde omnis iste natus error sit voluptatem accusantium doloremque laudantium, totam rem aperiam eaque ipsa, quae ab illo inventore veritatis et quasi architecto beatae vitae dicta sunt, explicabo.</p>
  </section>

  <footer class="site-footer">
    <div class="footer-nav">
      <div class="footer-heading">Navigation</div>
      <ul>
        <li>Home</li><li>About</li><li>Why Quarvolindex</li><li>Services</li><li>Solutions</li><li>Partners</li><li>Contact Us</li>
      </ul>
    </div>
    <div class="testimonial">
      <div class="footer-heading">Testimonial</div>
      <svg class="testimonial-icon" width="46" height="44" viewBox="0 0 46 44" aria-hidden="true"><path d="M4 4h26a3 3 0 0 1 3 3v14a3 3 0 0 1-3 3H14l-7 6v-6H4a3 3 0 0 1-3-3V7a3 3 0 0 1 3-3z" fill="none" stroke="#c9cfd5" stroke-width="2"/><path d="M20 20h21a3 3 0 0 1 3 3v12a3 3 0 0 1-3 3h-2v5l-6-5H20a3 3 0 0 1-3-3V23a3 3 0 0 1 3-3z" fill="#c9cfd5"/><text x="10" y="19" font-family="Arial,sans-serif" font-size="15" font-weight="700" fill="#c9cfd5">“</text><text x="25" y="36" font-family="Arial,sans-serif" font-size="15" font-weight="700" fill="#6e7985">”</text></svg>
      <blockquote>At vero eos et accusamus et iusto odio dignissimos ducimus, qui blanditiis praesentium voluptatum deleniti atque corrupti, quos dolores et quas molestias excepturi sint.”</blockquote>
      <cite><span>-</span> Dara Velmont</cite>
    </div>
    <div class="contact">
      <div class="footer-heading">Contact Us</div>
      <div class="social"><span></span><span></span><span></span><span></span><span></span></div>
      <p class="newsletter-note">subscribe to our monthly newsletter<br>and get the best deals and discounts</p>
      <div class="newsletter-field">enter email address</div>
      <div class="subscribe"><svg width="10" height="8" viewBox="0 0 10 8" aria-hidden="true"><path d="M0 0l10 4-10 4 2-4z" fill="#fff"/></svg>subscribe now</div>
    </div>
  </footer>
</div>
</body>
</html>
```